Brisbane IT support business needs our first letterhead (Contest)

Hello we are a Brisbane based Information Technology company providing support and services to small and medium sized businesses. We provide a range of services and solutions.

The business name is Harlowe Network Computing Services, or HNCS for short.

I am looking for a letterhead that looks professional (don't we all want that), but most importantly, it most utilize the colours in the logo attached, and any text used preferably in font type: HandelGotDBol.

```html
<!DOCTYPE html>
<html lang="en">
<head>
<meta charset="utf-8">
<title>HNCS Stationery – Folder and Letterhead</title>
<link rel="stylesheet" href="https://fonts.googleapis.com/css2?family=Michroma&family=Open+Sans:wght@400;600&family=Libre+Baskerville:ital@1&display=swap">
<style>
  :root {
    --navy: #0f4663;
    --orange: #ee7d22;
    --ink: #2a2a2a;
    --muted: #555;
    --paper: #ffffff;
    --ghost: #ececec;
    --backdrop: #e9e6e2;
  }
  * { box-sizing: border-box; margin: 0; padding: 0; }
  html, body { width: 1200px; height: 1024px; overflow: hidden; }
  body {
    background: var(--backdrop);
    position: relative;
    font-family: "Open Sans", Arial, sans-serif;
    color: var(--ink);
  }
  .sheet {
    position: absolute;
    background: var(--paper);
    box-shadow: 0 4px 14px rgba(0,0,0,.18);
    overflow: hidden;
  }

  /* Folder cover */
  .folder { left: 42px; top: 100px; width: 542px; height: 766px; }
  .folder-top { position: absolute; left: 0; top: 0; width: 100%; height: 250px; background: var(--navy); }
  .folder-skyline {
    position: absolute; left: 0; top: 250px; width: 100%; height: 150px;
    background: linear-gradient(to bottom, var(--navy) 0%, #6f93a6 45%, var(--paper) 100%);
  }
  .folder-brand {
    position: absolute; left: 128px; top: 580px;
    display: flex; align-items: center; gap: 18px;
  }
  .brand-dot { border-radius: 50%; background: var(--navy); flex: none; }
  .folder-brand .brand-dot { width: 104px; height: 104px; }
  .brand-name { font-family: "Michroma", sans-serif; color: var(--orange); line-height: 1; }
  .brand-name .abbr { display: block; }
  .brand-name .full { display: block; text-transform: uppercase; }
  .folder-brand .abbr { font-size: 44px; letter-spacing: 1px; }
  .folder-brand .full { font-size: 9.4px; margin-top: 8px; max-width: 200px; line-height: 1.3; }
  .folder-web {
    position: absolute; left: 0; width: 100%; top: 714px; text-align: center;
    font-size: 12px; font-weight: 600; color: #333; letter-spacing: .3px;
  }

  /* Letterhead */
  .letter { left: 611px; top: 102px; width: 545px; height: 770px; }
  .letter-brand { position: absolute; left: 58px; top: 58px; display: flex; align-items: center; gap: 10px; }
  .letter-brand .brand-dot { width: 62px; height: 62px; }
  .letter-brand .abbr { font-size: 25px; }
  .letter-brand .full { font-size: 5.4px; margin-top: 4px; max-width: 110px; line-height: 1.3; }
  .contact { position: absolute; left: 319px; top: 58px; font-size: 9px; line-height: 12.4px; color: var(--muted); }
  .contact .label { color: var(--orange); }
  .recipient { position: absolute; left: 62px; top: 189px; font-size: 10.8px; line-height: 13px; color: var(--ink); }
  .letter-body { position: absolute; left: 62px; top: 285px; width: 458px; font-size: 7.9px; line-height: 11.3px; color: #333; text-align: justify; }
  .letter-body .salutation { margin-bottom: 8px; }
  .letter-body p { margin-bottom: 11px; }
  .sign-off { font-size: 8px; line-height: 11px; color: #333; }
  .signature { font-family: "Libre Baskerville", Georgia, serif; font-style: italic; font-size: 10.5px; line-height: 14px; }
  .letter-skyline {
    position: absolute; left: 0; top: 560px; width: 100%; height: 188px;
    background: linear-gradient(to bottom, var(--paper) 0%, var(--ghost) 55%, #e4e4e4 100%);
  }
  .footer-bar { position: absolute; top: 748px; height: 22px; }
  .footer-bar.navy { left: 0; width: 380px; background: var(--navy); }
  .footer-bar.orange { left: 388px; right: 0; background: var(--orange); }
</style>
</head>
<body>

<section class="sheet folder">
  <div class="folder-top"></div>
  <div class="folder-skyline" role="img" aria-label="White city skyline silhouette with a suspension bridge"></div>
  <div class="folder-brand">
    <span class="brand-dot"></span>
    <span class="brand-name"><span class="abbr">HNCS</span><span class="full">Harlowe Network Computing Services</span></span>
  </div>
  <p class="folder-web">www.harlowenetworkcomputing.com</p>
</section>

<section class="sheet letter">
  <div class="letter-brand">
    <span class="brand-dot"></span>
    <span class="brand-name"><span class="abbr">HNCS</span><span class="full">Harlowe Network Computing Services</span></span>
  </div>

  <address class="contact" style="font-style:normal">
    2207 Kelvin Grove Road, Brisbane,<br>
    QLD 4059, Australia<br>
    <span class="label">P</span> : 07 3184 5520<br>
    <span class="label">F</span> : 07 3184 5521<br>
    <span class="label">E</span> : office@hncs-support.com<br>
    <span class="label">W</span> : www.hncs-support.com
  </address>

  <div class="recipient">Name<br>Title<br>Company Name<br>Address<br>City,State, Zip Code</div>

  <div class="letter-skyline" role="img" aria-label="Faint grey city skyline with a suspension bridge"></div>

  <div class="letter-body">
    <p class="salutation">Dear Nora Whitfield</p>
    <p>Lorem Ipsum is simply dummy text of the printing and typesetting industry. Lorem Ipsum has been the industry's standard dummy text ever since the 1500s, when an unknown printer took a galley of type and scrambled it to make a type specimen book. It has survived not only five centuries, but also the leap into electronic typesetting, remaining essentially unchanged. It was popularised in the 1960s with the release of Transferline sheets containing Lorem Ipsum passages, and more recently with desktop publishing software like Quillset Composer including versions of Lorem Ipsum.</p>
    <p>Contrary to popular belief, Lorem Ipsum is not simply random text. It has roots in a piece of classical Latin literature from 45 BC, making it over 2000 years old. Rowan Ellery, a Latin professor at Fairmont Hill College, looked up one of the more obscure Latin words, consectetur, from a Lorem Ipsum passage, and going through the cites of the word in classical literature, discovered the undoubtable source.</p>
    <p>Lorem Ipsum comes from sections 1.10.32 and 1.10.33 of "de Finibus Bonorum et Malorum" (The Extremes of Good and Evil) by Varenus, written in 45 BC. This book is a treatise on the theory of ethics, very popular during the Renaissance. The first line of Lorem Ipsum, "Lorem ipsum dolor sit amet..", comes from a line in section 1.10.32</p>
    <p>The standard chunk of Lorem Ipsum used since the 1500s is reproduced below for those interested. Sections 1.10.32 and 1.10.33 from "de Finibus Bonorum et Malorum" by Varenus are also reproduced in their exact original form, accompanied by English versions from the 1914 translation by T. Marwick.</p>
    <div class="sign-off">
      Sciencierly,<br>
      <span class="signature">Your Signature</span><br>
      Your name goes here<br>
      consultant manager
    </div>
  </div>

  <div class="footer-bar navy"></div>
  <div class="footer-bar orange"></div>
</section>

</body>
</html>
```